Corrowin Sack operates across the US and Australasia providing calico bags to small business through to large enterprise across all verticals. Our bags are the most premium in the market place and our customer service is second to none. Our competitive advantage lays in our competitive pricing, superior quality and outstanding customer service.

Industry/Entity Type

Business

Contact Information for Business Card

Corrowin Sack
Marisol Quenby
Managing Director
marisol@corrowinsack.com
www.corrowinsack.com.au
Mobile:- 0471 896 305
Level 3, 284 Harwick Street
Melbourne Victoria Australia 3000

```html
<!DOCTYPE html>
<html lang="en">
<head>
<meta charset="utf-8">
<title>Corrowin Sack — Business Card</title>
<link href="https://fonts.googleapis.com/css2?family=Questrial&display=swap" rel="stylesheet">
<style>
  :root {
    --backdrop: #d6dfdf;
    --card: #ffffff;
    --mint: #2fd69b;
    --card-shadow: rgba(40, 60, 60, 0.18);
  }
  * { box-sizing: border-box; margin: 0; padding: 0; }
  html, body {
    width: 1200px;
    height: 740px;
    overflow: hidden;
    background: var(--backdrop);
    font-family: "Questrial", "Century Gothic", sans-serif;
    color: var(--mint);
  }
  .canvas {
    position: relative;
    width: 1200px;
    height: 740px;
  }
  .card {
    position: absolute;
    width: 510px;
    height: 312px;
    background: var(--card);
    box-shadow: 0 10px 28px var(--card-shadow);
  }
  .card--front { left: 50px; top: 120px; }
  .card--back  { left: 640px; top: 308px; }

  /* Front */
  .brand-mark {
    position: absolute;
    left: 50%;
    top: 50%;
    transform: translate(-50%, -50%);
    display: flex;
    flex-direction: column;
    align-items: center;
    gap: 14px;
  }
  .brand-mark__square {
    width: 26px;
    height: 26px;
    border: 1.5px solid var(--mint);
  }
  .brand-mark__name {
    font-size: 24px;
    letter-spacing: 0.5px;
  }

  /* Back */
  .person {
    position: absolute;
    right: 34px;
    top: 34px;
    text-align: right;
  }
  .person__name {
    font-size: 22px;
    letter-spacing: 0.3px;
  }
  .person__role {
    font-size: 10.5px;
    margin-top: 2px;
  }
  .company {
    position: absolute;
    left: 36px;
    top: 150px;
    display: flex;
    align-items: center;
    gap: 10px;
  }
  .company__square {
    width: 16px;
    height: 16px;
    border: 1.3px solid var(--mint);
  }
  .company__name {
    font-size: 18px;
  }
  .contact-list {
    position: absolute;
    left: 36px;
    top: 190px;
    list-style: none;
  }
  .contact-list__item {
    display: flex;
    align-items: center;
    gap: 9px;
    font-size: 10.5px;
    height: 21px;
  }
  .contact-list__icon {
    width: 13px;
    height: 13px;
    flex: none;
  }
</style>
</head>
<body>
<main class="canvas">

  <section class="card card--front" aria-label="Card front">
    <div class="brand-mark">
      <span class="brand-mark__square"></span>
      <span class="brand-mark__name">Corrowin Sack</span>
    </div>
  </section>

  <section class="card card--back" aria-label="Card back">
    <div class="person">
      <p class="person__name">Marisol Quenby</p>
      <p class="person__role">Managing Director</p>
    </div>

    <div class="company">
      <span class="company__square"></span>
      <span class="company__name">Corrowin Sack</span>
    </div>

    <ul class="contact-list">
      <li class="contact-list__item">
        <svg class="contact-list__icon" viewBox="0 0 14 14" aria-hidden="true">
          <rect x="3.5" y="1" width="7" height="12" rx="1.2" fill="none" stroke="currentColor" stroke-width="1.2"/>
          <line x1="6" y1="11" x2="8" y2="11" stroke="currentColor" stroke-width="1.2"/>
        </svg>
        <span>0471 896 305</span>
      </li>
      <li class="contact-list__item">
        <svg class="contact-list__icon" viewBox="0 0 14 14" aria-hidden="true">
          <rect x="1" y="3" width="12" height="8.5" fill="none" stroke="currentColor" stroke-width="1.1"/>
          <polyline points="1,3 7,8 13,3" fill="none" stroke="currentColor" stroke-width="1.1"/>
        </svg>
        <span>marisol@corrowinsack.com</span>
      </li>
      <li class="contact-list__item">
        <svg class="contact-list__icon" viewBox="0 0 14 14" aria-hidden="true">
          <circle cx="7" cy="7" r="5.6" fill="none" stroke="currentColor" stroke-width="1.1"/>
          <ellipse cx="7" cy="7" rx="2.4" ry="5.6" fill="none" stroke="currentColor" stroke-width="1"/>
          <line x1="1.4" y1="7" x2="12.6" y2="7" stroke="currentColor" stroke-width="1"/>
        </svg>
        <span>www.corrowinsack.com.au</span>
      </li>
      <li class="contact-list__item">
        <svg class="contact-list__icon" viewBox="0 0 14 14" aria-hidden="true">
          <polygon points="7,1.5 13,7 11.3,7 11.3,12.5 2.7,12.5 2.7,7 1,7" fill="currentColor"/>
          <rect x="5.8" y="9" width="2.4" height="3.5" fill="#ffffff"/>
        </svg>
        <span>Level 3, 284 Harwick Street Melbourne Victoria Australia 3000</span>
      </li>
    </ul>
  </section>

</main>
</body>
</html>
```